KVO-Business Card Design

I need a modern, professional business card design that includes my logo as the main feature, maybe the entire background with the contact info overlaying or even contact info on the back and the logo full frontal

Neat and organized placement of contact information

Would like to see options in black and white

Target Market(s)

real estate Developers, Construction managers, business and home owners

Industry/Entity Type

Construction

Contact Information for Business Card

KVO Construction
Danny Ferrante
General Contractor

Office: 1-888-902-7315 Ext #1
Cell: 215-730-4162
Fax: 1-888-902-7315

Font styles to use
Serif

Requirements
Must have
• title
• office #
• cell #
• Email
• website
Nice to have
• fax

```html
<!DOCTYPE html>
<html lang="en">
<head>
<meta charset="utf-8">
<title>KVO Construction – Business Card</title>
<link rel="stylesheet" href="https://fonts.googleapis.com/css2?family=Source+Sans+3:wght@300;400;600&display=swap">
<style>
  :root {
    --backdrop: #3e5842;
    --card-white: #ffffff;
    --card-black: #050505;
    --brand-green: #6cc04a;
    --logo-green: #4fbf3a;
    --ink: #1a1a1a;
  }
  * { margin: 0; padding: 0; box-sizing: border-box; }
  html, body {
    width: 1200px; height: 800px; overflow: hidden;
    background: var(--backdrop);
    font-family: "Source Sans 3", "Helvetica Neue", Arial, sans-serif;
  }
  .sheet { position: relative; width: 1200px; height: 800px; }

  .card {
    position: absolute; top: 250px;
    width: 520px; height: 300px;
    background: var(--card-white);
    overflow: hidden;
    box-shadow: 0 14px 30px rgba(0,0,0,.35);
  }
  .card-front { left: 50px; }
  .card-back { left: 630px; }

  /* Front: logo panel + contact strip */
  .logo-panel {
    position: absolute; left: 0; top: 0; width: 100%; height: 178px;
    background: var(--card-black);
    display: flex; align-items: center; justify-content: center; gap: 14px;
  }
  .brand-mark {
    width: 22px; height: 22px; background: var(--logo-green);
  }
  .brand-name {
    color: var(--logo-green);
    font-weight: 600;
    font-size: 46px;
    letter-spacing: 1px;
  }
  .contact-strip {
    position: absolute; left: 0; top: 178px; width: 100%; height: 122px;
    display: flex; justify-content: space-between;
    padding: 20px 28px 0 26px;
  }
  .contact-list { list-style: none; }
  .contact-list li {
    display: flex; align-items: center; gap: 9px;
    font-size: 15px; color: var(--ink); line-height: 27px;
  }
  .contact-list.secondary { padding-top: 26px; }
  .contact-list svg { width: 14px; height: 14px; flex: none; fill: var(--ink); }

  /* Back: name band + logo box */
  .name-band {
    position: absolute; left: 0; top: 74px; width: 338px; height: 64px;
    background: var(--brand-green);
    padding: 12px 0 0 28px; color: var(--card-white);
  }
  .person-name {
    font-weight: 300; font-size: 26px; line-height: 28px; letter-spacing: -.3px;
  }
  .person-title {
    font-weight: 400; font-size: 9px; letter-spacing: .4px; margin-top: 1px;
  }
  .logo-box {
    position: absolute; left: 338px; top: 128px; width: 160px; height: 76px;
    background: var(--card-black);
    display: flex; align-items: center; justify-content: center; gap: 6px;
  }
  .logo-box .brand-mark { width: 8px; height: 8px; }
  .logo-box .brand-name { font-size: 17px; letter-spacing: .3px; }
</style>
</head>
<body>
<main class="sheet">

  <section class="card card-front" aria-label="Business card front">
    <div class="logo-panel">
      <span class="brand-mark"></span>
      <span class="brand-name">KVO Construction</span>
    </div>
    <div class="contact-strip">
      <ul class="contact-list primary">
        <li>
          <svg viewBox="0 0 16 16" aria-hidden="true"><path d="M3 2h3l1 3-2 1c1 2 2 3 4 4l1-2 3 1v3c0 1-1 2-2 2C6 14 2 10 2 4c0-1 0-2 1-2z"/></svg>
          1-888-902-7315 Ext #1
        </li>
        <li>
          <svg viewBox="0 0 16 16" aria-hidden="true"><rect x="4" y="1" width="8" height="4"/><rect x="1" y="6" width="14" height="6" rx="1"/><rect x="4" y="10" width="8" height="5"/></svg>
          1-888-902-7315
        </li>
        <li>
          <svg viewBox="0 0 16 16" aria-hidden="true"><path d="M1 2h14v9H1zM2.5 3.5v6h11v-6z" fill-rule="evenodd"/><rect x="6" y="12" width="4" height="2"/></svg>
          www.kvoconstruction.com
        </li>
      </ul>
      <ul class="contact-list secondary">
        <li>
          <svg viewBox="0 0 16 16" aria-hidden="true"><path d="M4 1h8v14H4zM5.5 3v9h5V3z" fill-rule="evenodd"/></svg>
          215-730-4162
        </li>
        <li>
          <svg viewBox="0 0 16 16" aria-hidden="true"><path d="M1 3h14v10H1zM2 4l6 5 6-5" fill-rule="evenodd"/><path d="M2.5 4.5 8 9l5.5-4.5v7h-11z" fill="#fff"/></svg>
          danny@kvoconstruction.com
        </li>
      </ul>
    </div>
  </section>

  <section class="card card-back" aria-label="Business card back">
    <div class="name-band">
      <p class="person-name">DANNY FERRANTE</p>
      <p class="person-title">GENERAL CONTRACTOR</p>
    </div>
    <div class="logo-box">
      <span class="brand-mark"></span>
      <span class="brand-name">KVO Construction</span>
    </div>
  </section>

</main>
</body>
</html>
```